Webpage needed for a new legal recruitment/headhunting companyi

I would like a professional and sharp looking website to showcase a new legal headhunting/recruitment company called Ridgel. The logo for the company is attached.

I like the following websites:
http://www.brimvaleadvisory.co.uk/
(For the general style and layout- although photographs of the team will be difficult as we don't have one yet!;-))

http://qomd.co.uk/
I like the style of the photographs etc on this one.

NB the pictures attached below are for information only- I don't think I would be able to use any of them...

Hope you can help!
Many thanks

```html
<!DOCTYPE html>
<html lang="en">
<head>
<meta charset="utf-8">
<title>Ridgel Legal Recruitment</title>
<link href="https://fonts.googleapis.com/css2?family=Open+Sans:ital,wght@0,400;0,600;0,700;1,600&display=swap" rel="stylesheet">
<style>
:root{
  --purple:#4a2a66;
  --purple-dark:#3e2257;
  --purple-soft:#5b3a78;
  --orange:#d2601c;
  --text:#3a3a3a;
  --muted:#6b6b6b;
  --rule:#e6e6e6;
  --pale:#fbf8fa;
  --white:#ffffff;
}
*{box-sizing:border-box;margin:0;padding:0}
html,body{width:703px;height:1200px;overflow:hidden}
body{position:relative;background:var(--white);font-family:"Open Sans",Arial,sans-serif;color:var(--text)}
.abs{position:absolute}
ul{list-style:none}
a{color:inherit;text-decoration:none}
h1,h2,h3,h4,h5{font-weight:400}

/* header */
.brand{left:96px;top:8px;width:130px;height:40px;display:flex;align-items:center;gap:6px}
.brand-mark{width:16px;height:16px;border-radius:50%;background:var(--purple)}
.brand-name{font-size:26px;font-weight:400;color:var(--purple);letter-spacing:1px;line-height:1}
.brand-tag{left:140px;top:36px;font-size:6px;color:var(--purple)}
.search{left:521px;top:10px;width:85px;height:13px;background:#f1f1f1;border:1px solid #e4e4e4}
.search svg{position:absolute;right:3px;top:2px}
.main-nav{left:270px;top:31px;display:flex;font-size:10.5px;color:var(--purple);white-space:nowrap}
.main-nav li+li::before{content:"|";margin:0 8px}

/* hero */
.hero{left:0;top:57px;width:703px;height:210px;background:linear-gradient(100deg,#3a3d4a 0%,#6b6a7a 20%,#2c2a36 40%,#5a4428 65%,#b88a2e 80%,#3a2c22 100%)}
.hero-person{left:100px;top:57px;width:170px;height:210px;background:linear-gradient(180deg,#6a5b52 0%,#a7c0dc 55%,#8fb0d4 100%)}
.sub-nav{left:188px;top:59px;width:370px;height:14px;background:var(--orange);display:flex;justify-content:center;align-items:center;font-size:7px;color:var(--white);white-space:nowrap}
.sub-nav li+li::before{content:"|";margin:0 5px}
.case{left:267px;top:85px;width:293px;height:94px;background:rgba(74,42,102,.88);color:var(--white);padding:6px 8px}
.case-tag{display:inline-block;background:var(--purple-dark);font-size:6px;font-weight:700;padding:2px 5px}
.case h2{font-size:9.5px;font-weight:400;margin-top:5px}
.case h3{font-size:6.5px;font-weight:700;margin-top:3px}
.case p{font-size:6.5px;line-height:10px;margin-top:6px}
.case b{font-size:5.5px}
.btn{background:var(--purple);color:var(--white);font-weight:600;display:flex;align-items:center;justify-content:center;white-space:nowrap}
.btn-consult{left:445px;top:190px;width:161px;height:31px;font-size:10px}
.inquire{left:682px;top:59px;width:21px;height:67px;background:var(--purple);color:var(--white)}
.inquire span{position:absolute;left:3px;bottom:6px;font-size:7px;writing-mode:vertical-rl;transform:rotate(180deg)}
.inquire i{position:absolute;left:3px;top:3px;width:15px;height:15px;border-radius:50%;border:1.5px solid var(--white);font-size:8px;font-style:normal;text-align:center;line-height:12px}

/* register */
.strip{left:0;width:703px;height:6px;background:#ededed}
.btn-reg{top:274px;width:129px;height:25px;font-size:8.5px;box-shadow:0 2px 0 #c9c1cf}

/* welcome */
.welcome-title{left:0;top:316px;width:703px;text-align:center;font-size:12.5px;color:var(--purple);letter-spacing:.3px}
.col{top:339px;width:207px;font-size:7.8px;line-height:12px;text-align:justify;letter-spacing:-.05px}
.col p+p{margin-top:12px}

/* opportunities */
.section-title{left:0;width:703px;text-align:center;font-size:12.5px;color:var(--orange)}
.job{top:521px;width:112px}
.job h4{font-size:7px;color:var(--muted)}
.job .pay{font-size:7px;font-weight:700;color:var(--purple);margin-top:1px}
.job p{font-size:6.5px;line-height:9px;color:var(--muted);margin-top:2px;white-space:nowrap}
.job .more{font-size:6.8px;font-weight:700;color:var(--orange);margin-top:6px}
.chev{width:16px;height:24px}

/* team */
.team{left:0;top:615px;width:703px;height:218px;background:var(--purple)}
.team-title{left:0;top:627px;width:703px;text-align:center;color:var(--white);font-size:11.5px}
.member{top:652px;width:160px;text-align:center;color:var(--white)}
.portrait{width:92px;height:92px;margin:0 auto;border-radius:50%;border:3px solid var(--purple-soft);background:radial-gradient(circle at 50% 40%,#d8d8d8,#8a8a8a)}
.member h4{font-size:10px;margin-top:14px;letter-spacing:.3px}
.member h5{font-size:8px;font-weight:700}
.member p{font-size:6.6px;font-weight:600;line-height:8.5px;margin-top:2px}
.member .contact{font-size:7.5px;margin-top:8px;display:block}
.to-top{font-size:7px;color:rgba(255,255,255,.2);text-align:center;width:24px}

/* success */
.success{left:0;top:833px;width:703px;height:142px;background:var(--pale)}
.story-photo{width:60px;height:60px;border-radius:50%;background:radial-gradient(circle at 50% 40%,#c79b82,#5a4a44)}
.story{top:887px;width:110px}
.story h4{font-size:7px;color:var(--muted)}
.story h4 i{font-weight:600}
.story p{font-size:6.4px;font-weight:600;line-height:9.5px;color:var(--muted);margin-top:1px;white-space:nowrap}
.story .more{font-size:7px;font-weight:700;color:var(--orange);margin-top:5px}

/* footer */
.footer{left:0;top:983px;width:703px;height:185px;background:var(--purple);color:var(--white)}
.f-brand{left:110px;top:991px;display:flex;align-items:center;gap:5px}
.f-brand .brand-mark{background:var(--white);width:13px;height:13px}
.f-brand .brand-name{color:var(--white);font-size:22px}
.f-brand-tag{left:150px;top:1013px;font-size:5px;color:var(--white)}
.f-col{top:1032px;color:var(--white)}
.f-col h4{font-size:8.3px;margin-bottom:3px}
.f-about p{font-size:8.3px;line-height:12px;width:130px}
.f-links li{font-size:7px;line-height:12px}
.f-site li{font-size:8.3px;line-height:12px;letter-spacing:.3px}
.f-contact li{font-size:7px;line-height:11px;display:flex;gap:5px}
.f-contact svg{flex:none;margin-top:1px}
.social{left:490px;top:1132px;display:flex;gap:4px}
.social span{width:20px;height:20px;border-radius:50%;background:var(--white)}
.legal{left:0;top:1168px;width:703px;height:32px;background:var(--orange);color:var(--white);font-size:6.8px;padding:10px 0 0 96px;white-space:nowrap}
</style>
</head>
<body>

<header>
  <div class="abs brand"><span class="brand-mark"></span><span class="brand-name">RIDGEL</span></div>
  <div class="abs brand-tag">Legal Recruitment</div>
  <div class="abs search"><svg width="8" height="8" viewBox="0 0 8 8"><circle cx="4.8" cy="3.2" r="2.2" fill="none" stroke="#4a2a66" stroke-width="1.2"/><line x1="3.2" y1="4.8" x2="1" y2="7" stroke="#4a2a66" stroke-width="1.3"/></svg></div>
  <ul class="abs main-nav"><li>CANDIDATES</li><li>CLIENTS</li><li>YOUR TEAM</li><li>ADVICE</li><li>CONTACT US</li></ul>
</header>

<section>
  <div class="abs hero" role="img" aria-label="Night city street with light trails and a lit clock tower"></div>
  <div class="abs hero-person" role="img" aria-label="Smiling consultant in shirt and tie"></div>
  <ul class="abs sub-nav"><li>CANDIDATES</li><li>WHAT WE'RE WORKING ON</li><li>RECENT SUCCESSES</li><li>TESTIMONIALS</li><li>ABROAD</li></ul>
  <svg class="abs chev" style="left:56px;top:143px" viewBox="0 0 16 24"><path d="M12 3 4 12l8 9" fill="none" stroke="rgba(255,255,255,.35)" stroke-width="4"/></svg>
  <svg class="abs chev" style="left:634px;top:143px" viewBox="0 0 16 24"><path d="M4 3l8 9-8 9" fill="none" stroke="rgba(255,255,255,.45)" stroke-width="4"/></svg>
  <article class="abs case">
    <span class="case-tag">CASE STUDIES</span>
    <h2>DANIEL HARLOW - BUSINESS DEVELOPMENT MANAGER</h2>
    <h3>HARLOW, PENN AND CARR</h3>
    <p>It was popularised in the 1960s with the release of Typeset sheets containing Lorem Ipsum passages, and more recently with desktop publishing software like Quarto Layout including versions of Lorem Ipsum. <b>READ MORE &gt;</b></p>
  </article>
  <a class="abs btn btn-consult">CONTACT A CONSULTANT &gt;</a>
  <div class="abs inquire"><i>?</i><span>INQUIRE</span></div>
</section>

<div class="abs strip" style="top:267px"></div>
<a class="abs btn btn-reg" style="left:178px">REGISTER AS A CANDIDATE &gt;</a>
<a class="abs btn btn-reg" style="left:396px">REGISTER AS A EMPLOYEE &gt;</a>
<svg class="abs" style="left:342px;top:293px" width="18" height="20" viewBox="0 0 18 20"><circle cx="10" cy="8" r="6" fill="none" stroke="#e2e2e2" stroke-width="2"/><line x1="6" y1="12" x2="2" y2="17" stroke="#e2e2e2" stroke-width="3"/></svg>

<section>
  <h1 class="abs welcome-title">WELCOME TO RIDGEL LEAGAL RECRUITMENT</h1>
  <div class="abs col" style="left:140px">
    <p>Lorem ipsum dolor sit amet, consectetuer adipiscing elit. Aenean commodo ligula eget dolor. Aenean massa. Cum sociis natoque penatibus et magnis dis parturient montes, nascetur ridiculus mus. Donec quam felis, ultricies nec, pellentesque eu, pretium quis, sem. Nulla consequat massa quis enim. Donec pede justo, fringilla vel, aliquet nec, vulputate eget, arcu.</p>
    <p>In enim justo, rhoncus ut, imperdiet a, venenatis vitae, justo. Nullam dictum felis eu pede mollis pretium. Integer tincidunt.</p>
  </div>
  <div class="abs col" style="left:357px">
    <p>Nullam dictum felis eu pede mollis pretium. Integer tincidunt. Cras dapibus. Vivamus elementum semper nisi. Aenean vulputate eleifend tellus. Aenean leo ligula, porttitor eu, consequat vitae, eleifend ac, enim.</p>
    <p>Aliquam lorem ante, dapibus in, viverra quis, feugiat a, tellus. Phasellus viverra nulla ut metus varius laoreet. Quisque rutrum. Aenean imperdiet. Aenean leo ligula, porttitor eu, consequat vitae, eleifend ac, enim. Aliquam lorem ante, dapibus in, viverra quis, feugiat a, tellus. Phasellus viverra nulla ut metus varius</p>
  </div>
</section>

<div class="abs strip" style="top:488px"></div>
<section>
  <h2 class="abs section-title" style="top:498px">LATEST OPPERTUNITIES</h2>
  <svg class="abs chev" style="left:54px;top:548px" viewBox="0 0 16 24"><path d="M12 3 4 12l8 9" fill="none" stroke="#e4e4e4" stroke-width="4"/></svg>
  <svg class="abs chev" style="left:632px;top:548px" viewBox="0 0 16 24"><path d="M4 3l8 9-8 9" fill="none" stroke="#e4e4e4" stroke-width="4"/></svg>
  <article class="abs job" style="left:96px"><h4>LEGAL OFFICERLEEDS</h4><div class="pay">£21,000 - £27,500</div><p>Dependant upon experience<br>Our client who are based in<br>Leeds, are a specialist law<br>firm in debt recovery and are<br>seeking to recruit a Legal..</p><div class="more">READ MORE &gt;</div></article>
  <article class="abs job" style="left:226px"><h4>LEGAL OFFICERLEEDS</h4><div class="pay">£21,000 - £27,500</div><p>Dependant upon experience<br>Our client who are based in<br>Leeds, are a specialist law<br>firm in debt recovery and are<br>seeking to recruit a Legal..</p><div class="more">READ MORE &gt;</div></article>
  <article class="abs job" style="left:357px"><h4>LEGAL OFFICERLEEDS</h4><div class="pay">£21,000 - £27,500</div><p>Dependant upon experience<br>Our client who are based in<br>Leeds, are a specialist law<br>firm in debt recovery and are<br>seeking to recruit a Legal..</p><div class="more">READ MORE &gt;</div></article>
  <article class="abs job" style="left:488px"><h4>LEGAL OFFICERLEEDS</h4><div class="pay">£21,000 - £27,500</div><p>Dependant upon experience<br>Our client who are based in<br>Leeds, are a specialist law<br>firm in debt recovery and are<br>seeking to recruit a Legal..</p><div class="more">READ MORE &gt;</div></article>
</section>
<div class="abs strip" style="top:610px"></div>

<section>
  <div class="abs team"></div>
  <h2 class="abs team-title">THE TEAM</h2>
  <div class="abs member" style="left:110px"><div class="portrait" role="img" aria-label="Black and white portrait of a director"></div><h4>TOM REEVE | DIRECTOR</h4><h5>FOR CLIENTS</h5><p>Lorem ipsum dolor sit amet<br>ces reters beered tetuer adipiscin.</p><span class="contact">CONTACT &gt;</span></div>
  <div class="abs member" style="left:272px"><div class="portrait" role="img" aria-label="Black and white portrait of a director"></div><h4>TOM REEVE | DIRECTOR</h4><h5>FOR CANDIDATES</h5><p>Lorem ipsum dolor sit amet<br>ces reters beered tetuer adipiscin.</p><span class="contact">CONTACT &gt;</span></div>
  <div class="abs member" style="left:435px"><div class="portrait" role="img" aria-label="Black and white portrait of a director"></div><h4>TOM REEVE | DIRECTOR</h4><h5>FOR GENERAL INQUIRIES</h5><p>Lorem ipsum dolor sit amet<br>ces reters beered tetuer adipiscin.</p><span class="contact">CONTACT &gt;</span></div>
  <div class="abs to-top" style="left:54px;top:792px"><svg width="22" height="12" viewBox="0 0 22 12"><path d="M2 10 11 2l9 8" fill="none" stroke="rgba(255,255,255,.2)" stroke-width="4"/></svg><div>TOP</div></div>
</section>

<section>
  <div class="abs success"></div>
  <h2 class="abs section-title" style="top:851px">SUCCESS STORIES FROM OUR CLIENTS</h2>
  <svg class="abs chev" style="left:54px;top:900px" viewBox="0 0 16 24"><path d="M12 3 4 12l8 9" fill="none" stroke="#dddddd" stroke-width="4"/></svg>
  <svg class="abs chev" style="left:632px;top:900px" viewBox="0 0 16 24"><path d="M4 3l8 9-8 9" fill="none" stroke="#dddddd" stroke-width="4"/></svg>
  <div class="abs story-photo" style="left:98px;top:884px" role="img" aria-label="Client portrait"></div>
  <div class="abs story-photo" style="left:271px;top:884px" role="img" aria-label="Client portrait"></div>
  <div class="abs story-photo" style="left:448px;top:884px" role="img" aria-label="Client portrait"></div>
  <article class="abs story" style="left:162px"><h4>NED CARVER - <i>Industries Ltd</i></h4><p>"Lorem ipsum dolor site<br>conseces reters beered<br>amet tetuer adipiscin."</p><div class="more">READ MORE &gt;</div></article>
  <article class="abs story" style="left:335px"><h4>NED CARVER - <i>Industries Ltd</i></h4><p>"Lorem ipsum dolor site<br>conseces reters beered<br>amet tetuer adipiscin."</p><div class="more">READ MORE &gt;</div></article>
  <article class="abs story" style="left:511px"><h4>NED CARVER - <i>Industries Ltd</i></h4><p>"Lorem ipsum dolor site<br>conseces reters beered<br>amet tetuer adipiscin."</p><div class="more">READ MORE &gt;</div></article>
</section>
<div class="abs strip" style="top:975px;height:8px"></div>

<footer>
  <div class="abs footer"></div>
  <div class="abs f-brand"><span class="brand-mark"></span><span class="brand-name">RIDGEL</span></div>
  <div class="abs f-brand-tag">Legal Recruitment</div>
  <div class="abs f-col f-about" style="left:96px"><h4>RIDGEL LEAGAL RECRUITMENT</h4><p>Lorem ipsum dolor sit amet, consectetuer adipiscing elit. Aenean commodo ligula eget dolor. Aenean massa. Cum sociis natoque penatibus et magnis dis parturient montes, nascetur ridiculus mus.</p></div>
  <div class="abs f-col" style="left:245px"><h4>CANDIDATES</h4><ul class="f-links"><li>CV WRITING</li><li>INTERVIEW ADVICE</li><li>NQ SOLICITORS</li><li>RECOMMEND A FRIEND</li><li>REGISTER ONLINE</li><li>REQUEST A CALLBACK</li><li>SALARY GUIDE</li><li>ISA REQUIREMENTS</li><li>SEND CV</li></ul></div>
  <div class="abs f-col" style="left:362px"><ul class="f-site"><li>HOME</li><li>ABOUT US</li><li>THE TEAM</li><li>CANDIDATES</li><li>ADVICE</li><li>SUCCSESS STORIES</li><li>CONTACT US</li></ul></div>
  <div class="abs f-col" style="left:490px"><h4>CONTACT US</h4>
    <ul class="f-contact">
      <li><svg width="8" height="11" viewBox="0 0 8 11"><rect x="1" y="0.5" width="6" height="10" rx="1" fill="none" stroke="#fff"/><line x1="3" y1="8.5" x2="5" y2="8.5" stroke="#fff"/></svg>020 7000 0000</li>
      <li><svg width="8" height="11" viewBox="0 0 8 11"><path d="M4 10.5C1.5 7 .5 5.5.5 4a3.5 3.5 0 0 1 7 0c0 1.5-1 3-3.5 6.5z" fill="#fff"/><circle cx="4" cy="4" r="1.3" fill="#4a2a66"/></svg><span>RIDGEL LEGAL RECRUITMENT<br>00 Mill Row<br>Ashmere, Essex<br>AM1 1AA</span></li>
      <li><svg width="11" height="8" viewBox="0 0 11 8"><rect width="11" height="8" fill="#fff"/><path d="M0 0l5.5 4.5L11 0" fill="none" stroke="#4a2a66"/></svg>info@ridgellegal.com</li>
    </ul>
  </div>
  <div class="abs social"><span></span><span></span><span></span><span></span></div>
  <div class="abs to-top" style="left:54px;top:1140px"><svg width="22" height="12" viewBox="0 0 22 12"><path d="M2 10 11 2l9 8" fill="none" stroke="rgba(255,255,255,.2)" stroke-width="4"/></svg><div>TOP</div></div>
  <div class="abs legal">© COPYRIGHT &nbsp;| TERMS OF USE &nbsp;| PRIVACY POLICY &nbsp;| SITEMAP &nbsp;| 2014 RIDGEL LEGAL RECRUITMENT &nbsp;| &nbsp;ALL RIGHTS RESERVED.</div>
</footer>

</body>
</html>
```